Modernization of existing web site

Update existing web site to a professional look vs a home-made site. Site look and navigation should be up to today's standards and display properly on mobile devices.
Only simple HTML and CSS is to be used as this is a basic site. No content management.
Existing site is https://www.plexumar.example

Target Market(s)

Insurance and Technology

Industry/Entity Type

Insurance and technology

Coding

Coded - Design and coding required

Number of Pages Required

5+ page

Font styles to use
Sans Serif

Colors
0054AA
0677BA
7BADD7
CADEEF
E8F1F8
0094D4
00A9DD
6FCCEA
C7EBF8
E9F6FB

Requirements
Must have
• A sleek, modern feel and also done with a button-downed industry in mind.
Nice to have
• Clean integration of the logo and name
Should not have
• Open to ideas

```html
<!DOCTYPE html>
<html lang="en">
<head>
<meta charset="utf-8">
<title>Plexumar — Business and Technology Strategy</title>
<link rel="stylesheet" href="https://fonts.googleapis.com/css2?family=Open+Sans:wght@400;600;700&display=swap">
<style>
:root{
  --blue-deep:#0054AA;
  --blue:#0677BA;
  --blue-bright:#1f7fd6;
  --blue-soft:#7BADD7;
  --blue-pale:#CADEEF;
  --blue-mist:#E8F1F8;
  --ink:#1d1d22;
  --text:#444;
  --muted:#8a8a8a;
  --line:#e3e3e3;
  --card:#f3f3f3;
  --white:#fff;
  --footer:#1e1e22;
}
*{box-sizing:border-box;margin:0;padding:0}
html,body{width:1200px;height:4556px;overflow:hidden}
body{font-family:"Open Sans",Arial,sans-serif;color:var(--text);background:var(--white);position:relative}
section,header,footer{position:absolute;left:0;width:1200px}
.center{text-align:center}
.eyebrow{font-size:9px;letter-spacing:3px;color:var(--blue);text-transform:uppercase;text-align:center}
.eyebrow::before,.eyebrow::after{content:"";display:inline-block;width:14px;height:1px;background:var(--blue-soft);vertical-align:middle;margin:0 8px}
.title{font-size:24px;font-weight:700;color:var(--ink);text-align:center;letter-spacing:.5px}
.lead{font-size:10.5px;color:var(--muted);text-align:center;line-height:1.5}
.pill{display:inline-block;border-radius:20px;font-size:8.5px;font-weight:600;letter-spacing:1px;text-transform:uppercase}
.pill-blue{background:var(--blue-bright);color:#fff;padding:8px 18px}
.abs{position:absolute}
.ring{position:absolute;border-radius:50%;background:#fff;box-shadow:0 2px 8px rgba(0,0,0,.12);display:flex;align-items:center;justify-content:center}
.brand{font-weight:700;color:#fff;font-size:21px;letter-spacing:.5px;display:flex;align-items:center;gap:8px}
.brand i{display:block;width:22px;height:22px;border-radius:50%;background:var(--blue-bright)}

/* hero */
.hero{top:0;height:589px}
.hero-bg{position:absolute;inset:0;background:radial-gradient(ellipse at 45% 45%,#2d5a96 0%,#17305c 45%,#0a1430 100%)}
.topbar{position:absolute;top:22px;left:130px;right:130px;height:26px;display:flex;align-items:center}
.nav{display:flex;gap:22px;margin-left:auto;font-size:8px;font-weight:600;color:#fff;text-transform:uppercase}
.nav .on{color:var(--blue-soft)}
.nav-phone{margin-left:30px;font-size:8px;font-weight:600;color:#fff;border-left:1px solid rgba(255,255,255,.3);padding-left:18px}
.nav-cta{margin-left:18px;padding:6px 14px;font-size:7.5px}
.hero-copy{position:absolute;top:212px;left:0;width:1200px;color:#fff;text-align:center}
.hero-copy .kicker{font-size:9px;letter-spacing:3px}
.hero-copy h1{font-size:31px;font-weight:600;line-height:38px;margin-top:16px}
.hero-copy p{font-size:10px;margin-top:12px}
.btn-white{background:#fff;color:var(--ink);padding:8px 18px;margin-top:18px}

/* services */
.services{top:589px;height:663px}
.filters{font-size:8.5px;font-weight:600;color:var(--ink);letter-spacing:.5px;text-align:center}
.filters span{margin:0 8px}
.filters .sep{color:var(--muted);font-weight:400}
.grid{position:absolute;top:207px;left:134px;display:grid;grid-template-columns:repeat(4,223px);gap:11px 12px}
.tile{height:122px;background:linear-gradient(#fafafa,#eeeeee);display:flex;flex-direction:column;align-items:center;justify-content:center;font-size:9.5px;color:var(--ink);text-align:center;line-height:1.4}
.tile svg{margin-bottom:10px}
.tile.active{background:var(--ink);color:#fff}

/* approach */
.approach{top:1252px;height:455px;background:linear-gradient(180deg,#f1f1f1,#fafafa 80%,#fff)}
.steps{position:absolute;top:180px;left:0;width:1200px}
.step{position:absolute;width:120px;text-align:center;font-size:7.5px;color:var(--muted);letter-spacing:.5px}
.step .ring{position:relative;width:52px;height:52px;margin:0 auto 10px}
.step.on .ring{background:var(--blue-bright)}
.step.on{color:var(--ink);font-weight:600}
.certs{top:1707px;height:150px;border-top:1px solid var(--line)}
.badges{position:absolute;top:44px;left:157px;display:flex;gap:18px}
.badge{width:162px;height:62px;background:#ececec;display:flex;align-items:center;justify-content:center}
.badge.on{background:#fff;box-shadow:0 2px 10px rgba(0,0,0,.12)}
.badge i{display:block;width:30px;height:30px;border-radius:50%;background:#bdbdbd}
.badge i.sq{border-radius:3px;width:40px;height:24px}

/* testimonials */
.voices{top:1857px;height:404px}
.voices-bg{position:absolute;inset:0;background:linear-gradient(90deg,#4b4d55,#6d6a68 40%,#3b3d45)}
.voices-copy{position:absolute;top:66px;width:1200px;color:#fff;text-align:center}
.voices-copy .eyebrow{color:#fff}
.voices-copy .title{color:#fff}
.avatar{width:52px;height:52px;border-radius:50%;margin:16px auto 0;background:#d9a483;border:2px solid #fff}
.quote{width:640px;margin:26px auto 0;font-size:12px;line-height:19px}
.stars{margin-top:14px;color:var(--blue-soft);font-size:10px;letter-spacing:5px}
.who{font-size:9.5px;margin-top:10px;line-height:16px}
.who b{font-weight:700}

/* focus */
.focus{top:2261px;height:569px}
.cards{position:absolute;top:166px;left:129px;display:flex;gap:19px}
.card{position:relative;width:221px;height:354px;color:#fff;text-align:center}
.card .label{position:absolute;bottom:40px;width:100%;font-size:8px;letter-spacing:1.5px;font-weight:600}
.card .ring{width:36px;height:36px;bottom:-18px;left:92px}
.card.dark{background:#2a2a2e;padding:22px 26px}
.card.dark h3{font-size:12px;font-weight:600;margin-top:10px}
.card.dark p{font-size:9px;line-height:14px;margin-top:6px}

/* about */
.about{top:2830px;height:505px}
.desk{position:absolute;left:129px;top:151px;width:461px;height:306px;background:linear-gradient(135deg,#e7e5e0,#bcb6ac 60%,#8d877f)}
.portrait{position:absolute;left:529px;top:237px;width:120px;height:120px;border-radius:50%;background:#7a6a5f;border:4px solid #fff;box-shadow:0 3px 10px rgba(0,0,0,.2)}
.bio{position:absolute;left:690px;top:152px;width:380px}
.bio h2{font-size:24px;font-weight:700;color:var(--ink);line-height:31px}
.bio p{font-size:9px;line-height:14.5px;color:var(--muted);margin-top:8px}
.bio b{color:var(--text);font-weight:600}

/* stats */
.stats{top:3335px;height:225px}
.stat{position:absolute;top:50px;width:200px;text-align:center}
.stat .ring{position:relative;width:56px;height:56px;margin:0 auto}
.stat .ring.dark{background:var(--ink)}
.stat strong{display:block;font-size:29px;font-weight:600;color:var(--ink);margin-top:16px}
.stat strong.hl{color:var(--blue-bright)}
.stat span{font-size:9px;color:var(--muted)}

/* help */
.help{top:3560px;height:270px}
.help-bg{position:absolute;inset:0;background:linear-gradient(90deg,#2b2c2f,#5d5d5f 50%,#2b2c2f)}
.help-copy{position:absolute;top:66px;width:1200px;text-align:center;color:#fff}
.help-copy .eyebrow{color:#ddd}
.help-copy .title{color:#fff}
.help-copy p{font-size:10px;line-height:16px;margin-top:8px}

/* contact */
.contact{top:3830px;height:363px}
.reach{position:absolute;top:170px;width:240px;text-align:center}
.reach .ring{position:relative;width:60px;height:60px;margin:0 auto}
.reach .ring.on{background:var(--blue-bright)}
.reach h4{font-size:11px;font-weight:700;color:var(--ink);margin-top:14px}
.reach h4.hl{color:var(--blue-bright)}
.reach p{font-size:9.5px;color:var(--blue-bright);margin-top:6px;line-height:15px}
.reach p.plain{color:var(--muted)}
.map{top:4193px;height:124px;background:linear-gradient(90deg,#2a74c8,#3b86d6 50%,#2a74c8)}

/* footer */
.footer{top:4317px;height:239px;background:var(--footer);color:#bbb;text-align:center}
.footer .brand{justify-content:center;margin-top:62px}
.footer small{display:block;font-size:7.5px;margin-top:14px;letter-spacing:.5px}
.links{font-size:8px;font-weight:600;color:#fff;margin-top:9px}
.links span{margin:0 14px}
.social{display:flex;justify-content:center;gap:12px;margin-top:14px;align-items:center}
.social i{display:block;width:12px;height:12px;border-radius:50%;background:#ddd}
.social i.on{width:22px;height:22px;background:var(--blue-bright)}
.tip{display:inline-block;font-size:7px;background:#fff;color:var(--ink);padding:2px 6px;margin-top:4px}
</style>
</head>
<body>

<header class="hero">
  <div class="hero-bg" role="img" aria-label="Dark blue photograph of a navigation compass dial"></div>
  <div class="topbar">
    <div class="brand"><i></i>PLEXUMAR</div>
    <nav class="nav"><span class="on">Home</span><span>Services</span><span>Strategy</span><span>Focus</span><span>Company</span><span>Contact</span></nav>
    <div class="nav-phone">555-014-2290</div>
    <span class="pill pill-blue nav-cta">Get Started</span>
  </div>
  <div class="hero-copy">
    <div class="kicker">BUSINESS AND TECHNOLOGY STRATEGY</div>
    <h1>NAVIGATING BUSINESS AND<br>TECHNOLOGY TO GENERATE RESULTS</h1>
    <p>At PLEXUMAR, we are here to assist you in realizing your vision for your business.</p>
    <span class="pill btn-white">Explore More</span>
  </div>
  <svg class="abs" style="left:594px;top:570px" width="12" height="8" viewBox="0 0 12 8"><path d="M1 1l5 5 5-5" stroke="#fff" fill="none" stroke-width="1.5"/></svg>
</header>

<section class="services">
  <div class="eyebrow" style="margin-top:68px">Services</div>
  <h2 class="title" style="margin-top:10px">WHAT WE DO</h2>
  <p class="lead" style="margin-top:6px">We offer a number of different services for insurance, technology, and financial services firms.</p>
  <div class="filters" style="margin-top:28px"><span style="color:var(--blue-bright)">ALL</span><span class="sep">/</span><span>INSURANCE</span><span class="sep">/</span><span>TECHNOLOGY</span><span class="sep">/</span><span>FINANCE</span></div>
  <div class="grid">
    <div class="tile"><svg width="18" height="18" viewBox="0 0 18 18"><circle cx="9" cy="9" r="6" stroke="#999" fill="none"/><circle cx="9" cy="9" r="2" stroke="#999" fill="none"/></svg>Business and Technology<br>Strategy</div>
    <div class="tile"><svg width="18" height="18" viewBox="0 0 18 18"><path d="M3 15l8-8m0 0l3-3" stroke="#999" fill="none"/></svg>Distribution Channel<br>Development</div>
    <div class="tile"><svg width="18" height="18" viewBox="0 0 18 18"><circle cx="9" cy="7" r="5" stroke="#999" fill="none"/><path d="M7 14h4" stroke="#999"/></svg>Rating and Regulatory</div>
    <div class="tile"><svg width="18" height="18" viewBox="0 0 18 18"><ellipse cx="9" cy="4" rx="6" ry="2" stroke="#999" fill="none"/><path d="M3 4v10c0 1 3 2 6 2s6-1 6-2V4" stroke="#999" fill="none"/></svg>Insurance Operations/Process</div>
    <div class="tile"><svg width="18" height="18" viewBox="0 0 18 18"><rect x="3" y="5" width="12" height="10" stroke="#999" fill="none"/><path d="M7 5V3h4v2" stroke="#999" fill="none"/></svg>M &amp; A Due Diligence</div>
    <div class="tile"><svg width="18" height="18" viewBox="0 0 18 18"><rect x="2" y="3" width="14" height="9" stroke="#999" fill="none"/><path d="M6 15h6" stroke="#999"/></svg>Data/Reporting/Analytics</div>
    <div class="tile active"><svg width="18" height="18" viewBox="0 0 18 18"><rect x="2" y="3" width="14" height="9" stroke="#3a8ee6" fill="none"/><path d="M6 15h6" stroke="#3a8ee6"/></svg>Technology Implementation</div>
    <div class="tile"><svg width="18" height="18" viewBox="0 0 18 18"><path d="M2 14l5-5 3 3 6-6" stroke="#999" fill="none"/></svg>Product Development</div>
    <div class="tile"><svg width="18" height="18" viewBox="0 0 18 18"><rect x="3" y="3" width="12" height="12" stroke="#999" fill="none"/><path d="M6 9l2 2 4-4" stroke="#999" fill="none"/></svg>Reinsurance</div>
    <div class="tile"><svg width="18" height="18" viewBox="0 0 18 18"><rect x="2" y="3" width="14" height="12" stroke="#999" fill="none"/><path d="M6 6v6M9 6v6M12 6v6" stroke="#999"/></svg>Catastrophe Risk Management</div>
    <div class="tile"><svg width="18" height="18" viewBox="0 0 18 18"><circle cx="9" cy="9" r="6" stroke="#999" fill="none"/><path d="M3 9h12M9 3c-3 3-3 9 0 12M9 3c3 3 3 9 0 12" stroke="#999" fill="none"/></svg>Enterprise Risk Management</div>
    <div class="tile"><svg width="18" height="18" viewBox="0 0 18 18"><rect x="2" y="2" width="10" height="10" stroke="#999" fill="none"/><rect x="6" y="6" width="10" height="10" stroke="#999" fill="#f3f3f3"/></svg>Interim Executive Leadership</div>
  </div>
</section>

<section class="approach">
  <div class="ring" style="left:574px;top:-26px;width:52px;height:52px"><svg width="20" height="20" viewBox="0 0 20 20"><circle cx="10" cy="10" r="7" stroke="#3a8ee6" fill="none" stroke-dasharray="3 2" stroke-width="2"/><circle cx="10" cy="10" r="3" stroke="#3a8ee6" fill="none"/></svg></div>
  <div class="eyebrow" style="margin-top:66px">Strategy</div>
  <h2 class="title" style="margin-top:8px">HOW WE DO IT</h2>
  <p class="lead" style="margin:6px auto 0;width:460px">We have extensive experience in many areas of business and technology combined with a deep level of integrity in the way we do business.</p>
  <div class="steps">
    <div class="step" style="left:200px"><div class="ring"><svg width="22" height="22"><rect x="3" y="3" width="16" height="16" stroke="#aaa" fill="none"/><path d="M7 15v-4M11 15V8M15 15v-6" stroke="#aaa"/></svg></div>PROGRAMS</div>
    <div class="step" style="left:370px"><div class="ring"><svg width="22" height="22"><rect x="3" y="4" width="16" height="14" stroke="#aaa" fill="none"/><path d="M6 8h10M6 12h10" stroke="#aaa"/></svg></div>TECHNOLOGIES</div>
    <div class="step on" style="left:539px"><div class="ring"><svg width="22" height="22"><circle cx="10" cy="10" r="6" stroke="#fff" fill="none" stroke-width="1.5"/><path d="M14 14l5 5" stroke="#fff" stroke-width="1.5"/></svg></div>RESEARCH</div>
    <div class="step" style="left:709px"><div class="ring"><svg width="22" height="22"><rect x="3" y="3" width="16" height="16" stroke="#aaa" fill="none"/><path d="M3 9h16M3 14h16M9 3v16M14 3v16" stroke="#aaa"/></svg></div>METHODOLOGY</div>
    <div class="step" style="left:878px"><div class="ring"><svg width="22" height="22"><rect x="3" y="4" width="16" height="11" stroke="#aaa" fill="none"/><path d="M8 19h6M11 15v4" stroke="#aaa"/></svg></div>PLANNING</div>
  </div>
  <svg class="abs" style="left:595px;top:264px" width="10" height="6"><path d="M1 1l4 4 4-4" stroke="#999" fill="none"/></svg>
  <h3 class="center" style="position:absolute;top:284px;width:1200px;font-size:14.5px;font-weight:700;color:var(--ink)">Prioritizing Existing Frameworks</h3>
  <p class="lead" style="position:absolute;top:312px;left:230px;width:740px">When an unknown printer took a galley of type and scrambled it to make a type specimen book. It has survived not only five centuries, but also the leap into electronic typesetting, remaining essentially unchanged.</p>
  <div class="center" style="position:absolute;top:364px;width:1200px"><span class="pill pill-blue">Contact Us Today!</span></div>
</section>

<section class="certs">
  <div class="eyebrow" style="margin-top:0;position:relative;top:-6px;background:#fff;display:block">Certifications</div>
  <div class="badges">
    <div class="badge"><i class="sq"></i></div>
    <div class="badge"><i></i></div>
    <div class="badge on"><i class="sq"></i></div>
    <div class="badge"><i></i></div>
    <div class="badge"><i class="sq"></i></div>
  </div>
</section>

<section class="voices">
  <div class="voices-bg" role="img" aria-label="Photograph of a business team smiling around a meeting table"></div>
  <div class="voices-copy">
    <div class="eyebrow">Testimonials</div>
    <h2 class="title" style="margin-top:10px">WHAT OUR CLIENTS SAY</h2>
    <div class="avatar" role="img" aria-label="Client portrait"></div>
    <p class="quote">“Lorem Ipsum is simply dummy text of the printing and typesetting industry. Lorem Ipsum has been the industry's standard dummy text ever since the 1500s, when an unknown printer took a galley of type and scrambled it to make a type specimen book.”</p>
    <div class="stars">★★★★★</div>
    <div class="who"><b>Peter</b><br>London</div>
  </div>
  <svg class="abs" style="left:210px;top:230px" width="10" height="16"><path d="M8 1L2 8l6 7" stroke="#fff" fill="none" stroke-width="1.5"/></svg>
  <svg class="abs" style="left:980px;top:230px" width="10" height="16"><path d="M2 1l6 7-6 7" stroke="#fff" fill="none" stroke-width="1.5"/></svg>
  <div class="ring" style="left:576px;top:378px;width:48px;height:48px;z-index:2"><svg width="20" height="20"><circle cx="10" cy="10" r="7" stroke="#3a8ee6" fill="none" stroke-width="1.5"/><circle cx="10" cy="10" r="3" fill="#3a8ee6"/></svg></div>
</section>

<section class="focus">
  <div class="eyebrow" style="margin-top:64px">Focus</div>
  <h2 class="title" style="margin-top:10px">WHY CHOOSE US</h2>
  <p class="lead" style="margin-top:6px">Gain the winning advantage in your industry!</p>
  <div class="cards">
    <div class="card" role="img" aria-label="Close-up photograph of program code on a dark screen" style="background:linear-gradient(160deg,#1c1d3a,#3a2f6a 50%,#14142a)"><div class="label">SERVICE</div><div class="ring"><svg width="14" height="14"><circle cx="7" cy="7" r="5" stroke="#3a8ee6" fill="none" stroke-dasharray="2 1.5" stroke-width="2"/></svg></div></div>
    <div class="card" role="img" aria-label="Photograph of a handshake over a laptop" style="background:linear-gradient(160deg,#8d8a86,#5d5b58 50%,#3d3b39)"><div class="label">CUSTOMER SATISFACTION</div><div class="ring"><svg width="14" height="14"><circle cx="7" cy="7" r="5.5" stroke="#3a8ee6" fill="none"/><path d="M4.5 8c1 1.5 4 1.5 5 0" stroke="#3a8ee6" fill="none"/></svg></div></div>
    <div class="card dark">
      <div style="width:22px;height:22px;border-radius:50%;background:#fff;margin:0 auto"></div>
      <h3>Pricing</h3>
      <p>Lorem Ipsum is simply dummy text of the printing and typesetting industry. Lorem Ipsum has been the industry's standard dummy text ever since the 1500s, when an unknown printer took a galley of type and scrambled it to make a type specimen book.</p>
      <svg class="abs" style="left:102px;bottom:16px" width="16" height="10"><path d="M1 9l5-5 3 3 6-6" stroke="#3a8ee6" fill="none"/></svg>
    </div>
    <div class="card" role="img" aria-label="Photograph looking up at glass office towers" style="background:linear-gradient(160deg,#a9c4d4,#4f7d93 50%,#1f3a48)"><div class="label">CHOICE</div><div class="ring"><svg width="14" height="14"><path d="M2 5h4l5-3v10l-5-3H2z" stroke="#3a8ee6" fill="none"/></svg></div></div>
  </div>
</section>

<section class="about">
  <div class="eyebrow" style="margin-top:32px">Company</div>
  <h2 class="title" style="margin-top:10px">ABOUT PLEXUMAR</h2>
  <p class="lead" style="margin:6px auto 0;width:460px">Plexumar was formed in late 2018 to bring over 35 years of experience in multiple industries and disciplines to our customers.</p>
  <div class="desk" role="img" aria-label="Photograph of a desk with coffee cup, keyboard and paperwork"></div>
  <div class="portrait" role="img" aria-label="Portrait of the founder"></div>
  <div class="bio">
    <h2>EXPERIENCE IN BUSINESS<br>AND TECHNOLOGY</h2>
    <p><b>Alan Merrow</b> has led large and small organizations. With senior executive experience in business and technology, he has a distinct view of the business and technology needs of organizations.</p>
    <p><b>Alan</b> has spent the last 20 years in various senior leadership positions at a leading property &amp; casualty insurance group, most recently as Chairman and President. He spent the early years of his career in high-tech manufacturing. He has also invested in several technology start-up's. Since 2011, <b>Alan</b> has served as an independent director at one of the nation's leading publicly traded financial services companies.</p>
    <p><b>Alan</b> holds the Chartered Property &amp; Casualty Underwriter (CPCU) and Associate in Reinsurance (ARe) designations. <b>Alan</b> also earned a master of business administration degree from Westbrook University, and a bachelor of science degree from Crestfield College.</p>
  </div>
</section>

<section class="stats">
  <div class="eyebrow" style="margin-top:8px">Experience</div>
  <div class="stat" style="left:140px"><div class="ring"><svg width="22" height="22"><rect x="3" y="4" width="16" height="15" stroke="#999" fill="none"/><path d="M3 8h16M7 11h2M11 11h2M15 11h1M7 15h2M11 15h2" stroke="#999"/></svg></div><strong>35</strong><span>years of experience</span></div>
  <div class="stat" style="left:380px"><div class="ring dark"><div style="width:20px;height:20px;border-radius:50%;background:#fff"></div></div><strong class="hl">100%</strong><span>Satisfied customers</span></div>
  <div class="stat" style="left:620px"><div class="ring"><svg width="22" height="22"><circle cx="7" cy="7" r="3.5" stroke="#999" fill="none"/><circle cx="15" cy="7" r="3.5" stroke="#999" fill="none"/><circle cx="7" cy="15" r="3.5" stroke="#999" fill="none"/><circle cx="15" cy="15" r="3.5" stroke="#999" fill="none"/></svg></div><strong>50+</strong><span>Teram Members</span></div>
  <div class="stat" style="left:860px"><div class="ring"><svg width="22" height="22"><rect x="3" y="6" width="16" height="13" stroke="#999" fill="none"/><path d="M8 6V3h6v3M3 12h16" stroke="#999" fill="none"/></svg></div><strong>1650+</strong><span>Project Completed</span></div>
</section>

<section class="help">
  <div class="help-bg" role="img" aria-label="Dark photograph of gears engraved with business words"></div>
  <div class="help-copy">
    <div class="eyebrow">Get Started</div>
    <h2 class="title" style="margin-top:8px">WE'RE HERE TO HELP</h2>
    <p>If you have any questions or requests about our company or the services we provide, please call<br>or email us, or use the form below.</p>
    <div style="margin-top:16px"><span class="pill pill-blue">✉&nbsp; Contact Us Today!</span></div>
  </div>
  <div class="ring" style="left:576px;top:246px;width:48px;height:48px;z-index:2"><svg width="18" height="18"><path d="M3 3h12l-4 6 4 6H3l4-6z" stroke="#3a8ee6" fill="none"/></svg></div>
</section>

<section class="contact">
  <div class="eyebrow" style="margin-top:68px">Contact</div>
  <h2 class="title" style="margin-top:8px">HOW TO REACH US</h2>
  <p class="lead" style="margin-top:6px">Lorem Ipsum is simply dummy text of the printing and typesetting industry.</p>
  <div class="reach" style="left:160px"><div class="ring"><svg width="22" height="22"><path d="M5 3l4 1 1 4-2 2c1 2 3 4 5 5l2-2 4 1 1 4-2 2C10 20 2 12 3 5z" stroke="#999" fill="none"/></svg></div><h4>Phone</h4><p>555-014-2290</p></div>
  <div class="reach" style="left:480px"><div class="ring on"><svg width="22" height="22"><path d="M11 20s-6-6-6-11a6 6 0 0112 0c0 5-6 11-6 11z" stroke="#fff" fill="none" stroke-width="1.5"/><circle cx="11" cy="9" r="2" stroke="#fff" fill="none"/></svg></div><h4 class="hl">Address</h4><p class="plain">42 Harbor Glen Ct,<br>Reno, NV 89501, USA</p></div>
  <div class="reach" style="left:800px"><div class="ring"><svg width="22" height="22"><rect x="3" y="6" width="16" height="12" stroke="#999" fill="none"/><path d="M3 6l8 6 8-6" stroke="#999" fill="none"/></svg></div><h4>Email</h4><p>info@plexumar.example</p></div>
</section>

<section class="map" role="img" aria-label="Street map showing the office location">
  <div class="ring" style="left:580px;top:42px;width:40px;height:40px;background:transparent;border:2px solid #fff;box-shadow:none"><svg width="16" height="16"><path d="M8 15s-5-5-5-8a5 5 0 0110 0c0 3-5 8-5 8z" stroke="#fff" fill="none"/></svg></div>
</section>

<footer class="footer">
  <div class="brand"><i></i>PLEXUMAR</div>
  <small>© COPYRIGHT 2022 PLEXUMAR LLC. ALL RIGHTS RESERVED</small>
  <div class="links"><span>CAREERS</span><span>PRIVACY POLICY</span></div>
  <div class="social"><i></i><i class="on"></i><i></i></div>
  <span class="tip">Follow</span>
  <svg class="abs" style="left:595px;top:218px" width="10" height="6"><path d="M1 5l4-4 4 4" stroke="#888" fill="none"/></svg>
</footer>

</body>
</html>
```